TALL Harborin business card design

We had logo design for New Investment company "Tall Harbor" office in Vietnam, Singapore. We would like to design te card " less is more" simple, humble but give the receiver a strong attention and trust

Ex
Lam Duc Thien
Chairman

Address:
Hanoi Office
The Lotus Court, #B305. Kela road, Ward Phuan 2, District North Sonven. Hanoi
Hochiminh city office
Daravo Commerce Tower, Level 37th. #5 Lo Bang st. District 1. Hochiminh City
Singapore office:
14 Pembury Road #05-02 Pembury Point Singapore 239417

M. .......
E: thien.lam@tallharbor.com.vn
W: www.tallharbor.com

Target Market(s)

Startup, partner....

Industry/Entity Type

Investment

Contact Information for Business Card

Lam Duc Thien
Chairman

Address:
Hanoi Office
Hochiminh city office
Singapore office:
M. .......
W: www.tallharbor.com

Colors

Designer to choose colors to be used in the design.

Requirements
Must have
• Less is more. Simple Humble elegant
Nice to have
• Less color, 2 or 1.
• TALL may have color ,the rest may greyscale

```html
<!DOCTYPE html>
<html lang="en">
<head>
<meta charset="utf-8">
<title>Tall Harbor business cards</title>
<link rel="stylesheet" href="https://fonts.googleapis.com/css2?family=Arimo:wght@400;700&display=swap">
<style>
  :root {
    --backdrop: #cccccc;
    --brand-blue: #1d75bd;
    --card-dark: #000000;
    --card-light: #ffffff;
    --text-soft: #d6d6d6;
    --text-white: #ffffff;
  }
  * { margin: 0; padding: 0; box-sizing: border-box; }
  html, body {
    width: 1200px; height: 842px; overflow: hidden;
    background: var(--backdrop);
    font-family: "Arimo", Arial, sans-serif;
  }
  .canvas { position: relative; width: 1200px; height: 842px; }
  .card {
    position: absolute; left: 341px; width: 524px; height: 291px;
    border-radius: 2px; overflow: hidden;
  }
  .card--dark { top: 144px; background: var(--card-dark); }
  .card--light { top: 476px; background: var(--card-light); }

  .wordmark {
    position: absolute; left: 44px; top: 30px; width: 96px;
    color: var(--brand-blue); font-weight: 700; text-align: center; line-height: 1;
  }
  .wordmark__main { display: block; font-size: 40px; letter-spacing: 1px; }
  .wordmark__sub { display: block; font-size: 11px; letter-spacing: 4.5px; margin-top: 4px; }

  .identity {
    position: absolute; right: 38px; top: 50px; text-align: right;
    font-size: 18px; line-height: 20px;
  }
  .card--dark .identity { color: var(--text-soft); }
  .card--light .identity { color: var(--brand-blue); }
  .identity__name { font-size: 20px; line-height: 24px; }
  .identity__role { font-weight: 700; }

  .offices {
    position: absolute; left: 0; top: 172px; width: 524px; height: 105px;
    background: var(--brand-blue); color: var(--text-white);
  }
  .office {
    position: absolute; top: 12px; text-align: right;
    font-size: 13px; line-height: 14.5px;
  }
  .office--hanoi { right: 370px; }
  .office--hcm { right: 187px; }
  .office--singapore { right: 35px; }
  .office__title { font-weight: 700; }
  .office__gap { margin-top: 3px; }
  .office__note { font-size: 10px; line-height: 12px; }
</style>
</head>
<body>
<main class="canvas">

  <section class="card card--dark">
    <div class="wordmark"><span class="wordmark__main">TALL</span><span class="wordmark__sub">HARBOR</span></div>
    <div class="identity">
      <div class="identity__name">Lam Duc Thien</div>
      <div class="identity__role">Chairman</div>
      <div>thien.lam@tallharbor.com.vn</div>
      <div>www.tallharbor.com</div>
    </div>
    <div class="offices">
      <div class="office office--hanoi">
        <div class="office__title">Hanoi Office</div>
        <div>The Lotus Court</div>
        <div>#B305. Kela road</div>
        <div>Ward Phuan 2</div>
        <div class="office__gap">District North Sonven</div>
        <div class="office__note">Hanoi Hochiminh city office</div>
      </div>
      <div class="office office--hcm">
        <div class="office__title">Hanoi Office</div>
        <div>Daravo Commerce Tower</div>
        <div>Level 37th</div>
        <div>#5 Lo Bang st. District 1</div>
        <div class="office__gap">Hochiminh City</div>
      </div>
      <div class="office office--singapore">
        <div class="office__title">Singapore office</div>
        <div>14 Pembury Road</div>
        <div>#05-02 Pembury Point</div>
        <div>Singapore 239417</div>
      </div>
    </div>
  </section>

  <section class="card card--light">
    <div class="wordmark"><span class="wordmark__main">TALL</span><span class="wordmark__sub">HARBOR</span></div>
    <div class="identity">
      <div class="identity__name">Lam Duc Thien</div>
      <div class="identity__role">Chairman</div>
      <div>thien.lam@tallharbor.com.vn</div>
      <div>www.tallharbor.com</div>
    </div>
    <div class="offices">
      <div class="office office--hanoi">
        <div class="office__title">Hanoi Office</div>
        <div>The Lotus Court</div>
        <div>#B305. Kela road</div>
        <div>Ward Phuan 2</div>
        <div class="office__gap">District North Sonven</div>
        <div class="office__note">Hanoi Hochiminh city office</div>
      </div>
      <div class="office office--hcm">
        <div class="office__title">Hanoi Office</div>
        <div>Daravo Commerce Tower</div>
        <div>Level 37th</div>
        <div>#5 Lo Bang st. District 1</div>
        <div class="office__gap">Hochiminh City</div>
      </div>
      <div class="office office--singapore">
        <div class="office__title">Singapore office</div>
        <div>14 Pembury Road</div>
        <div>#05-02 Pembury Point</div>
        <div>Singapore 239417</div>
      </div>
    </div>
  </section>

</main>
</body>
</html>
```